Brookmere Roofing Business Card

This is my current business card. But I’d like to make some changes. Somewhere on the card I’d like to list some of the services we offer. Maybe on the back? But I’d still like to keep the red. White and black modern look.

-residential & commercial roofing
-Roof Repairs & Maintenance
-Storm Damage & Insurance Claims specialist
-Christmas Lights and permanent Christmas lights
Fencing. Windows. Gutters. Siding. Sheetrock, painting.

```html
<!DOCTYPE html>
<html lang="en">
<head>
<meta charset="utf-8">
<title>Brookmere Roofing Business Card</title>
<link href="https://fonts.googleapis.com/css2?family=Quicksand:wght@500;600;700&family=Montserrat:wght@800&display=swap" rel="stylesheet">
<style>
  :root {
    --page: #2a2a2c;
    --card: #0c0c0c;
    --red: #e3141b;
    --red-dark: #8e0c10;
    --white: #ffffff;
    --soft: #e9e9e9;
  }
  * { box-sizing: border-box; margin: 0; padding: 0; }
  html, body { width: 1200px; height: 900px; overflow: hidden; }
  body {
    background: var(--page);
    font-family: "Quicksand", sans-serif;
    color: var(--white);
    position: relative;
  }
  .card {
    position: absolute;
    left: 250px;
    width: 700px;
    height: 400px;
    background: var(--card);
    border-radius: 22px;
    overflow: hidden;
  }
  .card--front { top: 40px; }
  .card--back { top: 465px; }
  .plaid-band {
    position: absolute;
    left: 0; right: 0; bottom: 0;
    height: 30px;
    background: linear-gradient(90deg, var(--red-dark), var(--red) 30%, var(--red-dark) 55%, var(--red) 80%, var(--red-dark));
  }

  /* Front */
  .brand {
    position: absolute;
    left: 60px; top: 120px;
    width: 270px;
    display: flex;
    flex-direction: column;
    align-items: center;
    gap: 18px;
  }
  .brand-mark {
    width: 110px; height: 110px;
    border-radius: 50%;
    background: var(--red);
  }
  .brand-name {
    font-weight: 700;
    font-size: 30px;
    line-height: 1.1;
    text-align: center;
    text-transform: uppercase;
    letter-spacing: 1px;
    color: var(--white);
  }
  .divider {
    position: absolute;
    left: 350px; top: 95px;
    width: 1px; height: 190px;
    background: var(--red);
  }
  .contact {
    position: absolute;
    left: 385px; top: 100px;
  }
  .person-name {
    font-family: "Montserrat", sans-serif;
    font-weight: 800;
    font-size: 32px;
    letter-spacing: 2px;
    color: var(--red);
    line-height: 1;
  }
  .person-role {
    font-size: 18px;
    font-weight: 500;
    letter-spacing: 1px;
    margin-top: 4px;
  }
  .contact-list { list-style: none; margin-top: 26px; }
  .contact-item {
    display: flex;
    align-items: center;
    gap: 10px;
    font-size: 19px;
    font-weight: 500;
    margin-bottom: 10px;
  }
  .contact-icon {
    width: 26px; height: 26px;
    border-radius: 50%;
    background: var(--red);
    display: flex; align-items: center; justify-content: center;
    flex-shrink: 0;
  }

  /* Back */
  .services {
    position: absolute;
    left: 0; right: 0; top: 78px;
    text-align: center;
    list-style: none;
    font-size: 21px;
    font-weight: 600;
    line-height: 1.45;
    color: var(--soft);
  }
  .rule {
    position: absolute;
    left: 110px; right: 110px; top: 252px;
    height: 1px;
    background: var(--red);
  }
  .trades {
    position: absolute;
    left: 0; right: 0; top: 272px;
    text-align: center;
    font-size: 16px;
    font-weight: 600;
    letter-spacing: 0.5px;
    text-transform: uppercase;
  }
  .trades .dot { color: var(--red); margin: 0 6px; }
</style>
</head>
<body>

<section class="card card--front">
  <div class="brand">
    <div class="brand-mark"></div>
    <div class="brand-name">Brookmere<br>Roofing Co.</div>
  </div>
  <div class="divider"></div>
  <div class="contact">
    <div class="person-name">NOLAN</div>
    <div class="person-role">OWNER</div>
    <ul class="contact-list">
      <li class="contact-item">
        <span class="contact-icon">
          <svg width="14" height="14" viewBox="0 0 24 24"><path fill="#fff" d="M6.6 10.8a15.1 15.1 0 0 0 6.6 6.6l2.2-2.2c.3-.3.7-.4 1-.2 1.1.4 2.3.6 3.6.6.6 0 1 .4 1 1V20c0 .6-.4 1-1 1A17 17 0 0 1 3 4c0-.6.4-1 1-1h3.5c.6 0 1 .4 1 1 0 1.3.2 2.5.6 3.6.1.3 0 .7-.2 1z"/></svg>
        </span>
        555-014-2298
      </li>
      <li class="contact-item">
        <span class="contact-icon">
          <svg width="14" height="14" viewBox="0 0 24 24"><rect x="2" y="5" width="20" height="14" rx="1" fill="#fff"/><path d="M2 6l10 7 10-7" fill="none" stroke="#e3141b" stroke-width="2"/></svg>
        </span>
        nolan@brookmereroofing.co
      </li>
      <li class="contact-item">
        <span class="contact-icon">
          <svg width="14" height="14" viewBox="0 0 24 24" fill="none" stroke="#fff" stroke-width="2"><circle cx="12" cy="12" r="9"/><path d="M3 12h18M12 3c3 3 3 15 0 18M12 3c-3 3-3 15 0 18"/></svg>
        </span>
        www.brookmereroofing.co
      </li>
    </ul>
  </div>
  <div class="plaid-band" role="img" aria-label="Red tartan plaid band along the bottom edge"></div>
</section>

<section class="card card--back">
  <ul class="services">
    <li>Residential &amp; Commercial Roofing</li>
    <li>Roof Repairs &amp; Maintenance</li>
    <li>Storm Damage &amp; Insurance Claims Specialist</li>
    <li>Christmas Lights and Permanent Christmas Lights</li>
  </ul>
  <div class="rule"></div>
  <p class="trades">Fencing<span class="dot">•</span>Windows<span class="dot">•</span>Gutters<span class="dot">•</span>Siding<span class="dot">•</span>Sheetrock<span class="dot">•</span>Painting.</p>
  <div class="plaid-band" role="img" aria-label="Red tartan plaid band along the bottom edge"></div>
</section>

</body>
</html>
```